Anzeigengestaltung für Workshops
Zielgruppe
Die KTW-Academy realisiert Workshops für Medienschaffende. Im konkreten Fall soll ein 1-tägiger Workshop für Sprecher*innen in Radio, Podcast und Voice-Over beworben werden.
Aufgabenstellung
Die Anzeige soll in den verschiedenen Social-Media-Kanälen ausgespielt werden. Sie soll cool sein, eher minimalistisch, keinesfalls verspielt oder knallig.
Textbausteine sind:
Die Kunst des ruhigen Atems bei Tag [das ist der Titel der Veranstaltung]
Wie Du gut rüberkommst als Sprecher*in in Radio, Podcast und Voice-Over [das ist die Unterzeile]
Präsenz-Training | KTW-Funkhaus | 15.9.2023 [das sind die Rahmendaten]
ggfs. mit Störer 'jetzt buchen' o.ä.
Logo und Bild der Trainerin sind verpflichtend

```html
<!DOCTYPE html>
<html lang="de">
<head>
<meta charset="utf-8">
<title>KTW-Academy – Die Kunst des ruhigen Atems bei Tag</title>
<link rel="stylesheet" href="https://fonts.googleapis.com/css2?family=Barlow+Condensed:wght@400&family=Fira+Sans+Extra+Condensed:wght@700;900&display=swap">
<style>
  :root {
    --green: #9bc421;
    --white: #ffffff;
    --black: #000000;
    --red: #c41012;
    --photo-light: #d9cfc0;
    --photo-dark: #3b3a33;
  }
  html, body {
    margin: 0;
    padding: 0;
    width: 1200px;
    height: 1200px;
    overflow: hidden;
    background: var(--green);
  }
  .ad {
    position: relative;
    width: 1200px;
    height: 1200px;
    overflow: hidden;
    background: var(--green);
    font-family: "Fira Sans Extra Condensed", sans-serif;
  }
  .title-band {
    position: absolute;
    left: 0;
    top: 104px;
    width: 1200px;
    height: 439px;
    background: var(--white);
  }
  .title {
    position: absolute;
    left: 74px;
    top: 58px;
    margin: 0;
    font-family: "Fira Sans Extra Condensed", sans-serif;
    font-weight: 900;
    font-size: 172px;
    line-height: 160px;
    letter-spacing: 1px;
    color: var(--black);
    white-space: nowrap;
    text-shadow: -8px -7px 0 var(--white);
  }
  .title span { display: block; }
  .speaker-shape {
    position: absolute;
    left: 0;
    top: 543px;
    width: 190px;
    height: 657px;
    background: var(--black);
    border-top-right-radius: 140px 120px;
  }
  .sound-waves {
    position: absolute;
    left: 0;
    top: 0;
    width: 1200px;
    height: 1200px;
    pointer-events: none;
  }
  .subline {
    position: absolute;
    left: 256px;
    top: 572px;
    width: 500px;
    margin: 0;
    font-family: "Barlow Condensed", sans-serif;
    font-weight: 400;
    font-size: 56px;
    line-height: 68px;
    color: var(--black);
    white-space: nowrap;
  }
  .subline span { display: block; }
  .booking-badge {
    position: absolute;
    left: 453px;
    top: 786px;
    width: 252px;
    height: 252px;
    border-radius: 50%;
    background: var(--red);
    display: flex;
    align-items: center;
    justify-content: center;
  }
  .booking-badge p {
    margin: 0;
    transform: rotate(-15deg);
    text-align: center;
    font-weight: 900;
    font-size: 54px;
    line-height: 56px;
    color: var(--white);
  }
  .trainer-photo {
    position: absolute;
    left: 797px;
    top: 393px;
    width: 355px;
    height: 383px;
    border-radius: 14px 14px 0 0;
    background: radial-gradient(ellipse at 55% 40%, var(--photo-light) 0%, #b7a98f 40%, #7f8a6a 70%, var(--photo-dark) 100%);
  }
  .brand {
    position: absolute;
    left: 797px;
    top: 776px;
    width: 355px;
    height: 150px;
    display: flex;
    align-items: center;
    justify-content: center;
    gap: 14px;
    background: var(--white);
    border-radius: 0 0 14px 14px;
  }
  .brand-mark {
    width: 26px;
    height: 26px;
    background: var(--green);
  }
  .brand-name {
    font-weight: 900;
    font-size: 56px;
    line-height: 1;
    color: var(--black);
    white-space: nowrap;
  }
  .event-facts {
    position: absolute;
    right: 57px;
    top: 1108px;
    margin: 0;
    font-weight: 700;
    font-size: 42px;
    line-height: 42px;
    color: var(--black);
    white-space: nowrap;
  }
</style>
</head>
<body>
  <main class="ad">
    <div class="title-band"></div>
    <h1 class="title">
      <span>Die Kunst des</span>
      <span>ruhigen Atems</span>
      <span>bei Tag</span>
    </h1>

    <div class="speaker-shape" role="img" aria-label="Schwarze Silhouette eines sprechenden Kopfes im Profil"></div>

    <svg class="sound-waves" viewBox="0 0 1200 1200" aria-hidden="true">
      <g fill="none" stroke="#000" stroke-width="19">
        <path d="M 274 919 A 50 50 0 0 1 274 1011"/>
        <path d="M 296 877 A 98 98 0 0 1 296 1053"/>
        <path d="M 328 834 A 152 152 0 0 1 328 1096"/>
      </g>
    </svg>

    <p class="subline">
      <span>Wie Du gut rüberkommst</span>
      <span>als Sprecher*in in Radio,</span>
      <span>Podcast und Voice-Over</span>
    </p>

    <div class="booking-badge"><p>JETZT<br>BUCHEN!</p></div>

    <div class="trainer-photo" role="img" aria-label="Porträtfoto der Trainerin"></div>

    <div class="brand">
      <span class="brand-mark"></span>
      <span class="brand-name">KTW-Academy</span>
    </div>

    <p class="event-facts">Präsenz-Training | KTW-Funkhaus | 15.9.2023</p>
  </main>
</body>
</html>
```